"Jewelry Line Postcard Design"

Would like to describe what the line is about via a bio include a photo of me and the logo.

Target Market(s)

20-55

Industry/Entity Type

Jewelry

```html
<!DOCTYPE html>
<html lang="en">
<head>
<meta charset="utf-8">
<title>Stele Vii – Jewelry Postcard</title>
<link rel="stylesheet" href="https://fonts.googleapis.com/css2?family=Open+Sans:ital,wght@0,400;0,700;1,400&family=Playfair+Display:ital@1&display=swap">
<style>
  :root {
    --page: #e9eaec;
    --plum: #3f0a3d;
    --plum-light: #6b1f66;
    --quote-ink: #ecd3e6;
    --bullet: #c98ac0;
    --white: #ffffff;
    --ink: #151515;
    --photo-light: #d9d9d9;
    --photo-dark: #5a5a5a;
  }
  * { margin: 0; padding: 0; box-sizing: border-box; }
  html, body {
    width: 1200px; height: 1000px; overflow: hidden;
    background: var(--page);
  }
  .postcard {
    position: absolute; left: 80px; top: 97px;
    width: 1040px; height: 805px;
    background: var(--plum);
    box-shadow: 3px 4px 8px rgba(0,0,0,.35);
    overflow: hidden;
  }
  .quote-band {
    position: absolute; left: 0; top: 51px;
    width: 993px; height: 120px;
    background: linear-gradient(90deg, var(--plum-light) 0%, #5a1656 40%, var(--plum) 100%);
    border: 2px dotted rgba(255,255,255,.55);
    border-left: none;
    padding: 14px 26px 0 60px;
  }
  .quote {
    font-family: "Playfair Display", Georgia, serif;
    font-style: italic;
    font-size: 22px; line-height: 28px;
    color: var(--quote-ink);
    text-align: right;
  }
  .bio {
    position: absolute; left: 50px; top: 200px; width: 625px;
    font-family: "Open Sans", Arial, sans-serif;
    font-size: 19px; line-height: 33px;
    color: var(--white);
    text-align: justify;
    list-style: none;
  }
  .bio li::before { content: "• "; color: var(--bullet); }
  .bio strong { font-weight: 700; }
  .portrait {
    position: absolute; left: 694px; top: 171px;
    width: 293px; height: 362px;
    border: 2px solid #e6e6e6;
    background: radial-gradient(ellipse at 50% 40%, var(--photo-light) 0%, #a9a9a9 55%, var(--photo-dark) 100%);
  }
  .product-band {
    position: absolute; left: 0; top: 588px;
    width: 100%; height: 158px;
    background: var(--white);
  }
  .brand {
    position: absolute; left: 55px; top: 0; width: 250px; height: 158px;
    display: flex; align-items: center; justify-content: center; gap: 10px;
  }
  .brand-name {
    font-family: "Open Sans", Arial, sans-serif;
    font-size: 30px; font-weight: 400; letter-spacing: 3px;
    color: var(--ink);
  }
  .brand-dot { width: 10px; height: 10px; border-radius: 50%; background: var(--ink); }
  .products { position: absolute; left: 0; top: 0; }
</style>
</head>
<body>
  <article class="postcard">
    <div class="quote-band">
      <p class="quote">“It’s my goal to make every woman feel like her very best self, so she can go out into the world to sparkle and shine. To create a line of jewelry that’s both beautiful and purposeful is truly a dream come true.”</p>
    </div>

    <ul class="bio">
      <li><strong>DR. LENA MARLOWE</strong> has had a love affair with jewelry for as long as she can remember. Perhaps it started way back in the day, when she religiously use to look through her grandmother’s jewelry box.</li>
      <li>Her current collection is <strong>STELE VII</strong> (<em>LIVING STARS</em> in Romanian). These pieces are based on the bold and dramatic costume pieces of the 60’s and 70’s. Everyone deserves to feel Glamorous and beautiful. This collection is a great way to step into your most stunning self.</li>
      <li>Dr. Lena’s jewelry has been worn by stylists, designers, high profile TV personalities and anchors, as well as people who just want to look good and feel beautiful.</li>
    </ul>

    <div class="portrait" role="img" aria-label="Black and white portrait of the designer"></div>

    <section class="product-band">
      <div class="brand">
        <span class="brand-name">STELE VII</span>
        <span class="brand-dot"></span>
      </div>
      <svg class="products" width="1040" height="158" viewBox="0 0 1040 158">
        <defs>
          <filter id="circle-shadow" x="-20%" y="-20%" width="140%" height="140%">
            <feDropShadow dx="3" dy="4" stdDeviation="4" flood-color="#000" flood-opacity=".3"/>
          </filter>
          <radialGradient id="gold" cx="50%" cy="50%" r="50%">
            <stop offset="0" stop-color="#e7b77a"/><stop offset="1" stop-color="#c98a45"/>
          </radialGradient>
          <radialGradient id="gunmetal" cx="50%" cy="50%" r="50%">
            <stop offset="0" stop-color="#8a8a8a"/><stop offset="1" stop-color="#4a4a4a"/>
          </radialGradient>
          <radialGradient id="bronze" cx="50%" cy="50%" r="50%">
            <stop offset="0" stop-color="#9c7c88"/><stop offset="1" stop-color="#5a3e48"/>
          </radialGradient>
          <radialGradient id="copper" cx="50%" cy="50%" r="50%">
            <stop offset="0" stop-color="#e0a262"/><stop offset="1" stop-color="#b06a2e"/>
          </radialGradient>
        </defs>
        <g filter="url(#circle-shadow)" fill="#fff">
          <circle cx="420" cy="70" r="82"/>
          <circle cx="585" cy="70" r="82"/>
          <circle cx="750" cy="70" r="82"/>
          <circle cx="903" cy="70" r="82"/>
        </g>
        <ellipse cx="420" cy="70" rx="40" ry="62" fill="url(#gold)" role="img" aria-label="Gold statement pendant"/>
        <ellipse cx="585" cy="70" rx="48" ry="55" fill="url(#gunmetal)" opacity=".8" role="img" aria-label="Gunmetal drop earrings"/>
        <ellipse cx="750" cy="70" rx="58" ry="56" fill="url(#bronze)" opacity=".8" role="img" aria-label="Bronze medallion earrings and necklace"/>
        <ellipse cx="903" cy="68" rx="52" ry="48" fill="url(#copper)" opacity=".8" role="img" aria-label="Copper chandelier earrings"/>
      </svg>
    </section>
  </article>
</body>
</html>
```